Do it yourself blood pressure poster and flyer

I work in a Drs Health Centre. We have a pod where patients can do their own blood pressure, height, weight etc. We'd like to design a poster and a flyer to encourage patients to use it. The poster would be on display in the waiting room and the flyer would be given to patients. Once in the pod, the measurements are easy to do and take less than 5 minutes.
Our name is Brynhafod Health Centre

Target Market(s)

Patinets in a deprived area, UK

Industry/Entity Type

Health Care

Requirements
Must have
• Eye catching; encourage patients to use self measurement of blood pressure
Nice to have
• Not too serious. Only takes a few minutes. Give result to Receptionist or Dr

```html
<!DOCTYPE html>
<html lang="en">
<head>
<meta charset="utf-8">
<title>Brynhafod Health Centre – Health Pod Flyer</title>
<link rel="stylesheet" href="https://fonts.googleapis.com/css2?family=Anton&family=Comfortaa:wght@500&family=Quicksand:wght@400;600&family=Open+Sans:wght@700&family=Tinos&display=swap">
<style>
  :root {
    --backdrop: #151515;
    --navy: #0f1b33;
    --orange: #ef6424;
    --white: #ffffff;
    --ink: #1a1a1a;
    --muted: #8a8c7e;
    --photo-light: #e6ecef;
    --photo-mid: #9fb4c4;
    --photo-dark: #4a5f78;
  }
  * { margin: 0; padding: 0; box-sizing: border-box; }
  html, body { width: 1200px; height: 840px; overflow: hidden; background: var(--backdrop); }
  .flyer {
    position: absolute; left: 330px; top: 40px;
    width: 540px; height: 760px;
    background: var(--white); overflow: hidden;
  }
  .flyer-shapes { position: absolute; inset: 0; }
  .pod-photo {
    position: absolute; left: 0; top: 150px; width: 540px; height: 420px;
    background: linear-gradient(100deg, var(--photo-light) 0%, var(--photo-mid) 45%, var(--photo-dark) 100%);
  }
  .headline {
    position: absolute; left: 40px; top: 34px;
    font-family: "Anton", sans-serif; font-size: 64px; line-height: 1;
    color: var(--white); letter-spacing: 0.5px;
  }
  .subline {
    position: absolute; left: 40px; top: 110px;
    font-family: "Quicksand", sans-serif; font-size: 19px; color: var(--white);
    letter-spacing: 0.8px;
  }
  .subline-highlight {
    position: absolute; left: 40px; top: 134px;
    font-family: "Quicksand", sans-serif; font-weight: 600; font-size: 36px;
    color: var(--orange); letter-spacing: 1px;
  }
  .centre-name {
    position: absolute; left: 30px; top: 542px;
    font-family: "Comfortaa", sans-serif; font-weight: 500; font-size: 36px;
    color: var(--ink); letter-spacing: 0.5px;
  }
  .body-copy {
    position: absolute; left: 40px; top: 640px; width: 460px;
    font-family: "Tinos", serif; font-size: 12px; line-height: 1.3;
    color: var(--ink); text-align: center;
  }
  .more-info {
    position: absolute; left: 0; top: 712px; width: 540px;
    display: flex; justify-content: center; align-items: center; gap: 10px;
    font-family: "Open Sans", sans-serif; font-weight: 700; font-size: 14px; color: var(--muted);
  }
  .social-mark { display: flex; align-items: center; gap: 6px; color: var(--muted); }
  .social-square { width: 18px; height: 18px; background: var(--muted); }
</style>
</head>
<body>
  <main class="flyer">
    <div class="pod-photo" role="img" aria-label="Photo of a patient seated in the white self-measurement health pod while a staff member works at a computer"></div>
    <svg class="flyer-shapes" viewBox="0 0 540 760" width="540" height="760" aria-hidden="true">
      <path d="M0 0 H540 V200 C430 230 330 250 220 240 C130 232 60 222 0 228 Z" fill="var(--navy)"/>
      <path d="M340 46 C430 60 500 85 540 112 V46 Z" fill="var(--orange)"/>
      <rect x="0" y="0" width="540" height="7" fill="var(--orange)"/>
      <path d="M0 520 C110 475 250 470 370 515 C440 540 500 552 540 548 V760 H0 Z" fill="var(--orange)"/>
      <path d="M0 530 C110 488 250 484 370 528 C440 554 500 566 540 562 V760 H0 Z" fill="var(--white)"/>
      <path d="M0 600 C120 588 260 590 380 600 C450 606 500 614 540 624" fill="none" stroke="var(--orange)" stroke-width="7"/>
    </svg>

    <h1 class="headline">Don’t Miss This..</h1>
    <p class="subline">The measurements are easy to do and take</p>
    <p class="subline-highlight">less than 5 minutes.</p>

    <h2 class="centre-name">Brynhafod Health Centre</h2>

    <p class="body-copy">Step into our health pod in the waiting room and check your own blood pressure, height and weight. It is quick, simple and private. Just follow the steps on the screen, print your results, then hand them to the Receptionist or your Doctor before you go home today.</p>

    <p class="more-info">More info at brynhafodhealth.co.uk
      <span class="social-mark"><span class="social-square"></span>Friendbook</span>
    </p>
  </main>
</body>
</html>
```